Upsell Vertical Banner Ad Design For B2B Marketing Agency Vertical 768px × 1180px IS THE SIZE

I need a banner made for my website www.brightlanepromotionhub.biz This banner will be an upsell advertisement for after someone signs up for my monthly program. When they login to their account for the 1st time I will give them the chance to upgrade their account to our annual program with just one click.

this is a page that upsells it currently to give you an idea how we market ourselves:
https://tlpx.pagevault-example.com/page/tlp-annual-upsell

Use this content:

Are You Ready To Commit To Taking Your Business To The Next Level?

Because We're In This For The Long-Haul and Dedicated To Your Success...

Save $300 By Upgrading To An Annual Membership And Pay Only $74/mth

((BUTTON))Yes, Upgrade My Plan Right Now!

*Must prepay the full year at only $898/yr!

Target Market(s)

business owners

Industry/Entity Type

Marketing

Requirements
Must have
• 768px × 1180px IS THE SIZE vertical

Use this content:

Nice to have
• Use this content:

Should not have
• Use this content:

```html
<!DOCTYPE html>
<html lang="en">
<head>
<meta charset="utf-8">
<title>Annual Membership Upgrade Banner</title>
<link rel="stylesheet" href="https://fonts.googleapis.com/css2?family=Fira+Sans:wght@500;600&family=PT+Sans:wght@400&display=swap">
<style>
  :root {
    --stage: #9c9c9c;
    --blue-top: #0e74d2;
    --blue-bottom: #0759a6;
    --green: #8dc63f;
    --green-light: #9fd150;
    --white: #ffffff;
    --photo-light: #e9e4dc;
    --photo-warm: #b89a82;
    --photo-dark: #6d5a52;
  }
  * { margin: 0; padding: 0; box-sizing: border-box; }
  html, body { width: 1100px; height: 1200px; overflow: hidden; background: var(--stage); }
  .banner {
    position: absolute; left: 166px; top: 10px;
    width: 768px; height: 1180px; overflow: hidden;
    background: linear-gradient(180deg, var(--blue-top) 40%, var(--blue-bottom) 100%);
    color: var(--white);
    font-family: "Fira Sans", sans-serif;
  }
  .banner__photo {
    position: absolute; left: 0; top: 0; width: 768px; height: 520px;
    background: linear-gradient(120deg, var(--photo-dark) 0%, var(--photo-warm) 25%, var(--photo-light) 55%, #f4f1ec 75%, var(--photo-warm) 100%);
  }
  .banner__wave { position: absolute; left: 0; top: 380px; width: 768px; height: 160px; }
  .headline {
    position: absolute; left: 0; top: 522px; width: 768px;
    text-align: center; font-weight: 600; font-size: 47px; line-height: 58px;
    text-transform: uppercase; letter-spacing: 0.3px;
    text-shadow: 0 2px 4px rgba(0,0,0,0.3);
  }
  .headline__accent { color: var(--green); }
  .tagline {
    position: absolute; left: 0; top: 720px; width: 768px; text-align: center;
    font-family: "PT Sans", sans-serif; font-size: 20px; letter-spacing: -0.2px;
  }
  .offer__frame { position: absolute; left: 0; top: 0; width: 768px; height: 1180px; }
  .offer__line {
    position: absolute; left: 0; width: 768px; text-align: center;
    font-weight: 600; text-transform: uppercase;
  }
  .offer__save { top: 808px; font-size: 37px; left: -12px; }
  .offer__detail { top: 880px; font-size: 27px; left: 0; letter-spacing: 0.2px; }
  .offer__price { top: 933px; font-size: 37px; left: -12px; }
  .cta {
    position: absolute; left: 98px; top: 1015px; width: 572px; height: 58px;
    border-radius: 29px; border: 2px solid rgba(255,255,255,0.85);
    background: linear-gradient(180deg, var(--green-light), var(--green));
    display: flex; align-items: center; justify-content: center;
    font-weight: 600; font-size: 26px; text-transform: uppercase; letter-spacing: -0.3px;
    box-shadow: 0 3px 6px rgba(0,0,0,0.25);
  }
  .footnote {
    position: absolute; left: 0; top: 1104px; width: 768px; text-align: center;
    font-family: "PT Sans", sans-serif; font-size: 23px;
  }
</style>
</head>
<body>
  <div class="banner">
    <div class="banner__photo" role="img" aria-label="Photo of a business team meeting around a table in a bright office with laptops"></div>
    <svg class="banner__wave" viewBox="0 0 768 160" aria-hidden="true">
      <path d="M0 160 L0 30 C150 -10 360 60 520 110 C620 140 720 130 768 80 L768 160 Z" fill="var(--green)"/>
      <path d="M0 160 L0 55 C150 15 360 70 520 118 C620 148 720 140 768 100 L768 160 Z" fill="var(--blue-top)"/>
    </svg>

    <h1 class="headline">
      Are You Ready To Commit To<br>
      <span class="headline__accent">Taking Your Business</span><br>
      To The Next Level?
    </h1>
    <p class="tagline">Because We're In This For The Long-Haul and Dedicated To Your Success...</p>

    <svg class="offer__frame" viewBox="0 0 768 1180" aria-hidden="true">
      <g stroke="var(--white)" stroke-width="3" fill="none">
        <polyline points="47,948 47,780 737,780 737,1043 670,1043"/>
        <polyline points="47,1023 47,1043 98,1043"/>
      </g>
    </svg>
    <p class="offer__line offer__save">Save $300</p>
    <p class="offer__line offer__detail">By Upgrading To An Annual Membership &amp;</p>
    <p class="offer__line offer__price">Pay Only $74/Mth</p>

    <div class="cta">Yes, Upgrade My Plan Right Now!</div>

    <p class="footnote">*Must prepay the full year at only $898/yr!</p>
  </div>
</body>
</html>
```